Book Title: THE QUIET LEDGER
Book Sub Title: Notes on forgotten harbours and the keepers who tended their lamps
Vibe: Professional, stylish, trustworthy (high-end men's fashion)
Website (for inspiration): www.velmorandpike.com
Attached: a potential photo to use for the cover, but open to other options (from our website)

```html
<!DOCTYPE html>
<html lang="en">
<head>
<meta charset="utf-8">
<title>The Quiet Ledger — Ellis Marroway</title>
<link rel="stylesheet" href="https://fonts.googleapis.com/css2?family=Montserrat:wght@300;400&family=Playfair+Display:wght@700;800&display=swap">
<style>
  :root {
    --paper: #fbf9f7;
    --taupe: #a59a8a;
    --charcoal: #3e3d3d;
    --ink: #3a393a;
    --photo-deep: #4a3426;
    --photo-mid: #8a6c52;
    --photo-light: #c9b49d;
  }
  html, body {
    margin: 0;
    padding: 0;
    width: 829px;
    height: 1200px;
    overflow: hidden;
    background: var(--paper);
  }
  .cover {
    position: relative;
    width: 829px;
    height: 1200px;
    background: var(--paper);
    overflow: hidden;
  }
  .cover-photo {
    position: absolute;
    left: 54px;
    top: 70px;
    width: 424px;
    height: 820px;
    border-radius: 40% 40% 18% 18% / 14% 14% 8% 8%;
    background:
      radial-gradient(ellipse at 50% 12%, var(--photo-deep) 0%, transparent 22%),
      radial-gradient(ellipse at 45% 40%, var(--photo-light) 0%, var(--photo-mid) 35%, transparent 70%),
      radial-gradient(ellipse at 50% 75%, var(--photo-deep) 0%, transparent 65%);
    opacity: 0.9;
  }
  .subtitle {
    position: absolute;
    right: 53px;
    top: 62px;
    margin: 0;
    text-align: right;
    font-family: "Montserrat", sans-serif;
    font-weight: 300;
    font-size: 23px;
    line-height: 33px;
    letter-spacing: 0.6px;
    color: var(--ink);
    text-transform: uppercase;
  }
  .title {
    position: absolute;
    left: 0;
    top: 0;
    width: 829px;
    height: 1200px;
  }
  .title text {
    font-family: "Playfair Display", serif;
    font-weight: 800;
  }
  .title .taupe { fill: var(--taupe); }
  .title .dark { fill: var(--charcoal); }
  .title .rule { stroke: var(--charcoal); stroke-width: 3; }
  .author {
    position: absolute;
    left: 0;
    width: 829px;
    top: 1073px;
    margin: 0;
    text-align: center;
    font-family: "Montserrat", sans-serif;
    font-weight: 400;
    font-size: 52px;
    letter-spacing: 5px;
    color: var(--ink);
  }
</style>
</head>
<body>
  <main class="cover">
    <div class="cover-photo" role="img" aria-label="Photograph of a seated man in a brown check jacket, waistcoat and fedora on a metal stool"></div>

    <p class="subtitle">Notes on forgotten<br>harbours and the keepers<br>who tended their lamps</p>

    <svg class="title" viewBox="0 0 829 1200" aria-label="The Quiet Ledger">
      <text class="taupe" x="485" y="572" font-size="112" textLength="304" lengthAdjust="spacingAndGlyphs">THE</text>
      <line class="rule" x1="472" y1="622" x2="558" y2="622"/>
      <text class="dark" x="566" y="637" font-size="55" textLength="213" lengthAdjust="spacingAndGlyphs">QUIET</text>
      <text class="taupe" x="66" y="871" font-size="290" textLength="713" lengthAdjust="spacingAndGlyphs">LED</text>
      <text class="dark" x="62" y="1034" font-size="190" textLength="720" lengthAdjust="spacingAndGlyphs">GER</text>
    </svg>

    <p class="author">ELLIS MARROWAY</p>
  </main>
</body>
</html>
```